KVR GUARDING WEBSITE BANNER DESIGN OF AWESOME

Please take a look at the attached Banner. I want a redesign Idea. The requirements are below.

1)Must Use Website Background
2)Must Use Photo Provided
3)Must Include Button
4)Website the banner will be used on you can see the current at the bottom of the page: https://b.pelmarox.com

Target Market(s)

Anyone Seeking Security Guard Services

```html
<!DOCTYPE html>
<html lang="en">
<head>
<meta charset="UTF-8">
<title>KVR Guarding – Get Secured Today</title>
<link href="https://fonts.googleapis.com/css2?family=League+Spartan:wght@600;700;800&family=Montserrat:wght@400;800&display=swap" rel="stylesheet">
<style>
  :root {
    --navy: #112c5a;
    --navy-deep: #0c1f42;
    --gold: #f0b022;
    --white: #ffffff;
    --steel: rgba(150, 165, 190, 0.55);
    --photo-dark: #0d1a33;
    --photo-mid: #1f3e6e;
    --photo-light: #5f86bd;
  }
  * { margin: 0; padding: 0; box-sizing: border-box; }
  html, body {
    width: 1200px;
    height: 675px;
    overflow: hidden;
    background: var(--navy);
  }
  .banner {
    position: relative;
    width: 1200px;
    height: 675px;
    background: var(--navy);
    overflow: hidden;
  }
  .banner__art {
    position: absolute;
    inset: 0;
    width: 1200px;
    height: 675px;
  }
  .banner__copy {
    position: absolute;
    left: 71px;
    top: 70px;
    width: 420px;
  }
  .headline {
    font-family: "League Spartan", sans-serif;
    font-weight: 700;
    font-size: 60px;
    line-height: 64px;
    color: var(--white);
    letter-spacing: 0.5px;
  }
  .tagline {
    margin-top: 38px;
    font-family: "League Spartan", sans-serif;
    font-weight: 600;
    font-size: 28px;
    line-height: 36px;
    color: var(--gold);
    letter-spacing: 0.4px;
  }
  .features {
    list-style: none;
    margin-top: 12px;
  }
  .features__item {
    display: flex;
    align-items: center;
    height: 50px;
    margin-bottom: 22px;
    font-family: "Montserrat", sans-serif;
    font-weight: 400;
    font-size: 22px;
    color: var(--white);
  }
  .features__tick {
    width: 50px;
    height: 50px;
    margin-right: 15px;
    flex: none;
  }
  .cta {
    position: absolute;
    left: 129px;
    top: 546px;
    width: 276px;
    height: 61px;
    border-radius: 31px;
    background: var(--gold);
    display: flex;
    align-items: center;
    justify-content: center;
    gap: 16px;
    font-family: "Montserrat", sans-serif;
    font-weight: 800;
    font-size: 20px;
    color: var(--navy);
    text-decoration: none;
    letter-spacing: 0.3px;
  }
  .cta__chevron { width: 16px; height: 28px; }
</style>
</head>
<body>
<main class="banner">
  <svg class="banner__art" viewBox="0 0 1200 675" xmlns="http://www.w3.org/2000/svg">
    <defs>
      <linearGradient id="photoTone" x1="0" y1="1" x2="1" y2="0">
        <stop offset="0" stop-color="var(--photo-dark)"/>
        <stop offset="0.5" stop-color="var(--photo-mid)"/>
        <stop offset="1" stop-color="var(--photo-light)"/>
      </linearGradient>
    </defs>
    <polygon class="hero-photo" role="img"
      aria-label="Photo: security guard seen from behind shining a flashlight up a dark stairwell"
      points="740,0 1200,0 1200,675 470,675" fill="url(#photoTone)"/>
    <polygon class="band band--steel" points="737,0 782,0 665,271 602,236" fill="var(--steel)"/>
    <polygon class="band band--gold" points="782,0 867,0 738,226 673,196" fill="var(--gold)"/>
    <polygon class="band band--steel" points="551,467 580,483 479,675 458,675" fill="var(--steel)"/>
    <polygon class="band band--gold" points="487,546 515,563 454,675 411,675" fill="var(--gold)"/>
    <polygon class="band band--steel" points="1101,527 1162,560 1117,675 1073,675" fill="var(--steel)"/>
    <polygon class="band band--gold" points="1053,568 1114,604 1073,675 988,675" fill="var(--gold)"/>
    <polygon class="corner" points="1200,499 1200,675 1101,675" fill="var(--navy)"/>
  </svg>

  <section class="banner__copy">
    <h1 class="headline">GET SECURED<br>TODAY</h1>
    <p class="tagline">WE TAKE YOUR SECURITY<br>PERSONAL</p>
    <ul class="features">
      <li class="features__item">
        <svg class="features__tick" viewBox="0 0 50 50"><circle cx="25" cy="25" r="25" fill="var(--gold)"/><path d="M14 25 L22 33 L36 18" fill="none" stroke="var(--navy)" stroke-width="5" stroke-linecap="round" stroke-linejoin="round"/></svg>
        Client Portal
      </li>
      <li class="features__item">
        <svg class="features__tick" viewBox="0 0 50 50"><circle cx="25" cy="25" r="25" fill="var(--gold)"/><path d="M14 25 L22 33 L36 18" fill="none" stroke="var(--navy)" stroke-width="5" stroke-linecap="round" stroke-linejoin="round"/></svg>
        24x7 Dispatch
      </li>
      <li class="features__item">
        <svg class="features__tick" viewBox="0 0 50 50"><circle cx="25" cy="25" r="25" fill="var(--gold)"/><path d="M14 25 L22 33 L36 18" fill="none" stroke="var(--navy)" stroke-width="5" stroke-linecap="round" stroke-linejoin="round"/></svg>
        No Binding Contracts
      </li>
    </ul>
  </section>

  <a class="cta" href="https://b.pelmarox.com">
    GET STARTED
    <svg class="cta__chevron" viewBox="0 0 16 28"><path d="M3 3 L13 14 L3 25" fill="none" stroke="var(--navy)" stroke-width="4" stroke-linecap="round" stroke-linejoin="round"/></svg>
  </a>
</main>
</body>
</html>
```